MJ's Sports Bar Menu (Cape Cod Sports Bar)

We are a new england sports bar based on Cape Cod.

We are an old school type sports bar with pizza and wings type food.

We want to highlight our pizza as the main draw on our menu.

The style we are looking for is a placemat menu that looks casual and fun.

We want the following sections:
Starters:

Soups:

Salads:

Handhelds:

Plates:

Sides:

Desserts:

I can provide a draft of all the menu items upon request didn't want to overload this text box thank you!

• The menu must be LANDSCAPE design as it is going on a paper placemat. It also needs to all fit on ONE SIDE.

```html
<!DOCTYPE html>
<html lang="en">
<head>
<meta charset="utf-8">
<title>MJ's Sports Bar Placemat Menu</title>
<link href="https://fonts.googleapis.com/css2?family=Inter:wght@400;500;600;700;800&display=swap" rel="stylesheet">
<style>
  :root {
    --navy: #253d4c;
    --paper: #dfe9f0;
    --paper-light: #eaf1f6;
    --red: #8e2a2e;
    --red-text: #9b2b2f;
    --ink: #2c3a44;
    --rule: #9fb0bb;
    --stage: #e4e4e4;
  }
  * { box-sizing: border-box; margin: 0; padding: 0; }
  html, body {
    width: 1200px; height: 2468px; overflow: hidden;
    background: var(--stage);
    font-family: "Inter", Arial, sans-serif;
    color: var(--ink);
  }
  .placemat {
    position: absolute; left: 50px; top: 845px;
    width: 1100px; height: 778px;
    background: var(--navy);
  }
  .placemat-paper {
    position: absolute; left: 20px; top: 20px; right: 20px; bottom: 20px;
    background: radial-gradient(ellipse at 40% 30%, var(--paper-light), var(--paper) 70%);
    overflow: hidden;
  }
  .brand-name {
    position: absolute; left: 30px; top: 34px; width: 240px;
    font-weight: 800; font-size: 28px; line-height: 1.1;
    color: var(--navy); letter-spacing: 0.3px;
  }

  .menu-section { position: absolute; }
  .section-title {
    position: relative; z-index: 2; display: inline-block;
    background: var(--navy); color: #fff;
    font-weight: 700; font-size: 16px; padding: 6px 18px; letter-spacing: 0.3px;
  }
  .section-note {
    position: relative; z-index: 1; display: table;
    margin: -18px 0 0 6px; padding: 21px 6px 5px 6px;
    border: 1px solid var(--red-text);
    color: var(--red-text); font-size: 10px; font-weight: 500;
    white-space: nowrap;
  }
  .item-list { list-style: none; margin-top: 9px; }
  .item-list li {
    height: 26px; display: flex; align-items: center; justify-content: space-between;
    font-size: 10.5px; border-bottom: 1px solid var(--rule); padding-top: 2px;
    white-space: nowrap;
  }
  .item-list li span:last-child { width: 44px; flex: none; }

  .pizza-panel {
    position: absolute; right: 0; top: 0; width: 245px; height: 100%;
    background: var(--red); border-top-left-radius: 20px; border-bottom-left-radius: 20px;
  }
  .pizza-title {
    position: absolute; left: 16px; top: 22px;
    background: var(--navy); color: #fff; white-space: nowrap;
    font-weight: 700; font-size: 16px; padding: 6px 12px; letter-spacing: 0.2px;
  }
  .pizza-note {
    position: absolute; left: 18px; top: 66px;
    color: #fff; font-weight: 700; font-size: 10px; white-space: nowrap;
  }
  .pizza-list {
    position: absolute; left: 16px; top: 92px; width: 213px; list-style: none;
  }
  .pizza-list li {
    height: 28px; display: flex; align-items: center; justify-content: space-between;
    padding: 0 6px 0 4px; color: #fff; font-weight: 700; font-size: 11px;
    border-bottom: 1px solid rgba(255,255,255,0.55);
  }
  .pizza-list li:last-child { border-bottom: none; }

  .food-photo { position: absolute; border-radius: 14px; }
  .food-photo.round { border-radius: 50%; }
</style>
</head>
<body>
<main class="placemat">
  <div class="placemat-paper">
    <h1 class="brand-name">MJ's Sports Bar</h1>

    <section class="menu-section" style="left:30px;top:120px;width:240px">
      <h2 class="section-title">PLATES</h2>
      <p class="section-note">Big portions. Game-day ready.</p>
      <ul class="item-list">
        <li><span>Fish &amp; Chips</span><span>$15.00</span></li>
        <li><span>Chicken Tenders &amp; Fries</span><span>$22.00</span></li>
        <li><span>Steak Tips with mashed potatoes</span><span>$15.00</span></li>
        <li><span>Wings Dinner (10 wings + side)</span><span>$22.00</span></li>
        <li><span>Mac &amp; Cheese</span><span>$15.00</span></li>
        <li><span>Buffalo Chicken Mac</span><span>$22.00</span></li>
      </ul>
    </section>

    <section class="menu-section" style="left:30px;top:370px;width:240px">
      <h2 class="section-title">SIDES</h2>
      <p class="section-note">Big portions. Game-day ready.</p>
      <ul class="item-list">
        <li><span>French Fries</span><span>$15.00</span></li>
        <li><span>Sweet Potato Fries</span><span>$22.00</span></li>
        <li><span>Onion Rings</span><span>$15.00</span></li>
        <li><span>Coleslaw</span><span>$22.00</span></li>
        <li><span>Mashed Potatoes</span><span>$15.00</span></li>
        <li><span>Side Salad</span><span>$22.00</span></li>
      </ul>
    </section>

    <section class="menu-section" style="left:300px;top:30px;width:240px">
      <h2 class="section-title">STARTERS</h2>
      <p class="section-note">Even better with beer.</p>
      <ul class="item-list">
        <li><span>Classic Chicken Wings</span><span>$15.00</span></li>
        <li><span>Boneless Wings</span><span>$22.00</span></li>
        <li><span>Mozzarella Sticks with marinara</span><span>$15.00</span></li>
        <li><span>Loaded Potato Skins</span><span>$22.00</span></li>
        <li><span>Fried Pickles with house dip</span><span>$15.00</span></li>
        <li><span>Garlic Bread with cheese</span><span>$22.00</span></li>
      </ul>
    </section>

    <section class="menu-section" style="left:300px;top:270px;width:240px">
      <h2 class="section-title">HANDHELDS</h2>
      <p class="section-note">Served with fries or chips.</p>
      <ul class="item-list">
        <li><span>Classic Cheeseburger</span><span>$15.00</span></li>
        <li><span>Bacon Cheeseburger</span><span>$22.00</span></li>
        <li><span>Fried Chicken Sandwich</span><span>$15.00</span></li>
        <li><span>Buffalo Chicken Wrap</span><span>$22.00</span></li>
        <li><span>Grilled Chicken Club</span><span>$15.00</span></li>
        <li><span>Fish Sandwich (Cape Cod favorite)</span><span>$22.00</span></li>
      </ul>
    </section>

    <section class="menu-section" style="left:300px;top:510px;width:240px">
      <h2 class="section-title">SALADS</h2>
      <p class="section-note">Add grilled or crispy chicken to any salad.</p>
      <ul class="item-list">
        <li><span>House Garden Salad</span><span>$15.00</span></li>
        <li><span>Caesar Salad</span><span>$22.00</span></li>
        <li><span>Greek Salad</span><span>$15.00</span></li>
        <li><span>Buffalo Chicken Salad</span><span>$22.00</span></li>
      </ul>
    </section>

    <section class="menu-section" style="left:570px;top:30px;width:220px">
      <h2 class="section-title">DESSERTS</h2>
      <p class="section-note">Save room... or don't.</p>
      <ul class="item-list">
        <li><span>Chocolate Lava Cake</span><span>$15.00</span></li>
        <li><span>Cheesecake</span><span>$22.00</span></li>
        <li><span>Warm Brownie Sundae</span><span>$15.00</span></li>
      </ul>
    </section>

    <section class="menu-section" style="left:570px;top:195px;width:220px">
      <h2 class="section-title">SOUPS</h2>
      <p class="section-note">Add grilled or crispy chicken to any salad.</p>
      <ul class="item-list">
        <li><span>New England Clam Chowder</span><span>$15.00</span></li>
        <li><span>Soup of the Day</span><span>$22.00</span></li>
      </ul>
    </section>

    <div class="food-photo" role="img" aria-label="Photo of glazed chicken wings" style="left:570px;top:335px;width:103px;height:180px;background:radial-gradient(circle,#b5472a,#d88a5a 75%);"></div>
    <div class="food-photo" role="img" aria-label="Photo of a crispy chicken burger" style="left:687px;top:335px;width:103px;height:180px;background:radial-gradient(circle,#d9a060,#e8cfa4 75%);"></div>
    <div class="food-photo" role="img" aria-label="Photo of a fresh green salad" style="left:570px;top:529px;width:103px;height:180px;background:radial-gradient(circle,#6e9f3e,#b9d18e 75%);"></div>
    <div class="food-photo" role="img" aria-label="Photo of a bowl of vegetable soup" style="left:687px;top:529px;width:103px;height:180px;background:radial-gradient(circle,#c9742e,#e6c08e 75%);"></div>

    <section class="pizza-panel">
      <h2 class="pizza-title">FAMOUS HOUSE PIZZA</h2>
      <p class="pizza-note">Our signature dough, hand-stretched daily.</p>
      <ul class="pizza-list">
        <li><span>Cheese Pizza</span><span>$15.00</span></li>
        <li><span>Pepperoni</span><span>$22.00</span></li>
        <li><span>Meat Lovers</span><span>$15.00</span></li>
        <li><span>Cape Cod Clam Pizza</span><span>$22.00</span></li>
        <li><span>Buffalo Chicken Pizza</span><span>$15.00</span></li>
        <li><span>Veggie</span><span>$22.00</span></li>
        <li><span>Build Your Own</span><span>$15.00</span></li>
      </ul>
      <div class="food-photo round" role="img" aria-label="Photo of a sliced vegetable pizza" style="left:22px;top:320px;width:200px;height:200px;background:radial-gradient(circle,#d9603a,#e2b070 75%);"></div>
      <div class="food-photo round" role="img" aria-label="Photo of a whole vegetable pizza" style="left:42px;top:540px;width:160px;height:160px;background:radial-gradient(circle,#d6583a,#e4b878 75%);"></div>
    </section>
  </div>
</main>
</body>
</html>
```